Energy and Environment Venture Capital Blog

Look for an out of the box creative design!

I am working on putting together a new blog / website with a few colleagues in the cleantech / energy venture capital space. I would like to push the box on design and get really creative for how to display the following (very simple):

1) Updated News on venture capital and cleantech (rss feed)
2) Would also like to have a profile page to feature "company of the month"
2.1) Included in this page I would like to be able to have a gallery of photos and have it be an interactive profile of company that includes:
2.1.1) Funding received to date, funders, location, founders (really good example of this is would be on greenmark.net. (there may even be a way to take the date right from their website)
EXTRA: would be amazing to be able to place all the selected company on a map
3) Blog entries that can include photos and movies and active commenting
4) Resources section for interesting websites, books, surveys etc. (pagepile)
5) Would like to be able to link my social media (chirpr, friendwall)

A couple good examples include:

http://www.blufinch.co.uk/
http://www.harvestloomworks.co.uk/
http://www.pine-quill.com/

Note: I have a logo designed for the website that I can send across. I also have a domain name registered at http://k7ledgering.com/

I have also attached the draft logo to show the colors I am hoping to use across the site.
Updates

Reason: Really want to make sure that we get the design right and dont want to have to rush things. If however I find a design concept I like I am happy to pull the trigger right away and work outside the contest.

Target Market(s)

venture capitalists, technologists, SMEs

Industry/Entity Type

Venture Capital

Requirements
Must have
• A funky and creative landing page
The profile page (I would like it to be called K7 Profiles) should be the feature section of the website
Nice to have
• What I was hoping to do (if possible) was to create a stock index that tracks some of the leading cleantech stocks on the market. Done know if there is anything out there that is open source but if there is I would love a section on the blog called "K7 Index"
Should not have
• The design should not use old-style, serif fonts like Times New Roman.

```html
<!DOCTYPE html>
<html lang="en">
<head>
<meta charset="utf-8">
<title>northvale</title>
<link href="https://fonts.googleapis.com/css2?family=Arimo:wght@400;700&display=swap" rel="stylesheet">
<style>
:root{
  --black:#000;
  --page:#fff;
  --ink:#333;
  --muted:#888;
  --link:#2a9bd6;
  --green:#6fb52c;
  --red:#cc1f1f;
  --footer:#b3b3b3;
  --footer-text:#f4f4f4;
  --brand:#4b4b4b;
}
*{margin:0;padding:0;box-sizing:border-box}
html,body{width:1200px;height:822px;overflow:hidden;background:var(--page)}
body{position:relative;font-family:"Arimo",Arial,sans-serif;color:var(--ink)}
.abs{position:absolute}
a{color:inherit;text-decoration:none}

.topbar{left:0;top:0;width:1200px;height:58px;background:var(--black)}
.skyline{left:185px;top:0;width:345px;height:66px;background:linear-gradient(180deg,#3a3a3a,#6a6a6a 70%,#8a8a8a)}
.top-social{left:843px;top:27px;display:flex;gap:4px}
.top-social span{width:10px;height:10px;background:var(--green)}

.brand-box{left:312px;top:40px;width:174px;height:52px;background:var(--page)}
.brand{display:flex;align-items:center;gap:8px;font-size:27px;color:var(--brand);letter-spacing:-.5px;white-space:nowrap}
.brand .mark{width:24px;height:24px;border:3px solid var(--brand);border-radius:3px}
.brand-main{left:326px;top:55px}
.tagline{left:317px;top:95px;font-size:6.6px;font-style:italic;color:var(--muted);white-space:nowrap}

.nav{left:541px;top:71px;display:flex;font-size:8.6px;font-weight:700;color:#333;white-space:nowrap}
.nav a{display:flex;align-items:center;gap:5px;margin-right:24px}
.nav .ico{width:17px;height:14px;border:2px solid #555;border-radius:2px}

.ticker-rule{left:317px;top:115px;width:566px;height:2px;background:#e4e4e4}
.regions{left:317px;top:124px;display:flex;flex-direction:column;gap:1px;font-size:6px;font-weight:700;color:#4a6a93}
.regions span{width:54px;height:11px;line-height:10px;padding-left:4px;background:linear-gradient(#fdfdfd,#e6e6e6);border:1px solid #c8c8c8;white-space:nowrap}
.regions .on{background:#fff;color:#222;width:60px}
.quote{font-size:7.6px;line-height:9.5px;white-space:nowrap}
.quote .name{color:#2c5e9e}
.quote .val{color:#111}
.quote .dn{color:var(--red)}
.quote .up{color:var(--green)}
.qline{height:2px;background:var(--red)}
.qline.up{background:var(--green)}
.more{left:864px;top:173px;font-size:6px;color:#2c5e9e}

.panel{border:2px solid #d6d6d6;background:var(--page)}
.panel h2{position:absolute;font-size:18px;font-weight:700;color:#333;letter-spacing:-.2px;white-space:nowrap}
.dots{position:absolute;display:flex;gap:2px}
.dots i{width:8px;height:8px;border-radius:50%;border:1px solid #9a9a9a}
.dots i.on{background:var(--green);border-color:var(--green)}
.small{font-size:7.3px;line-height:10.6px;color:#444}
.small b{color:#222}
.small .lk{color:var(--link);font-weight:700}
.view{position:absolute;font-size:7.5px;font-weight:700;color:var(--link);white-space:nowrap}

.news-item{margin-bottom:6px}
.photo{border:1px solid #d0d0d0}

.post-head{display:flex;align-items:center;font-size:7px;font-weight:700;color:#333;white-space:nowrap}
.post-head .sq{width:21px;height:18px;border:2px solid #666;border-radius:2px;margin-right:7px}
.post-head small{font-size:5px;font-weight:400;margin-left:3px}
.tiny{font-size:5.4px;line-height:8.3px;color:#444}
.count{display:inline-block;border:1px solid #888;padding:0 3px;font-size:5.5px;margin-left:6px}
.lorem{font-size:5.3px;line-height:7.6px;color:#444;letter-spacing:-.05px}

.footer{left:0;top:728px;width:1200px;height:94px;background:var(--footer)}
.foot-nav{left:318px;top:741px;display:flex;gap:14px;font-size:7px;color:var(--footer-text);white-space:nowrap}
.follow{left:822px;top:742px;font-size:7px;color:var(--footer-text)}
.foot-social{left:822px;top:755px;display:flex;gap:2px}
.foot-social span{width:10px;height:10px;background:#eee}
.brand-foot{left:553px;top:780px;font-size:23px;color:#4f4f4f}
.brand-foot .mark{width:22px;height:22px}
</style>
</head>
<body>

<div class="abs topbar"></div>
<div class="abs skyline" role="img" aria-label="City skyline silhouette"></div>
<div class="abs top-social"><span></span><span></span><span></span></div>

<div class="abs brand-box"></div>
<div class="abs brand brand-main"><span class="mark"></span>northvale</div>
<div class="abs tagline">Engaged discussions about energy &amp; environment venture capital</div>

<nav class="abs nav">
  <a href="#"><span class="ico"></span>Home</a>
  <a href="#"><span class="ico"></span>Profiles</a>
  <a href="#">Resources</a>
  <a href="#">About</a>
  <a href="#">Contact</a>
  <a href="#" style="margin-right:0">Blog</a>
</nav>

<div class="abs ticker-rule"></div>
<div class="abs regions">
  <span class="on">US</span><span>Europe</span><span>Asia</span><span>⚙ Customize</span>
</div>
<div class="abs" style="left:375px;top:171px;width:170px;height:2px;background:var(--red)"></div>
<div class="abs quote" style="left:380px;top:124px">
  <div class="name">Broad 500</div><div class="val">1,456.65</div><div class="dn">-5.24</div><div class="dn">-0.36%</div>
</div>
<svg class="abs" style="left:432px;top:122px" width="116" height="44" viewBox="0 0 116 44">
  <rect x="2" y="2" width="84" height="30" fill="#fff" stroke="#ddd"/>
  <line x1="2" y1="8" x2="86" y2="8" stroke="#e06060" stroke-width=".6"/>
  <path d="M2 20 L8 14 L14 24 L20 22 L26 26 L32 23 L38 27 L44 24 L50 26 L56 22 L62 20 L68 15 L74 17 L80 12 L86 10 L86 32 L2 32Z" fill="#cfe0f0"/>
  <path d="M2 20 L8 14 L14 24 L20 22 L26 26 L32 23 L38 27 L44 24 L50 26 L56 22 L62 20 L68 15 L74 17 L80 12 L86 10" fill="none" stroke="#3a6fb0" stroke-width="1"/>
  <g font-size="5" fill="#555" font-family="Arimo,Arial,sans-serif">
    <text x="90" y="6">1,465</text><text x="90" y="13">1,460</text><text x="90" y="23">1,455</text><text x="90" y="31">1,450</text>
    <text x="4" y="39">10am</text><text x="28" y="39">12pm</text><text x="52" y="39">2pm</text><text x="74" y="39">4pm</text>
  </g>
</svg>

<div class="abs quote" style="left:551px;top:124px"><div class="name">Indus 30</div><div class="val">13,327.13</div><div class="dn">-57.16</div><div class="dn">-0.43%</div></div>
<div class="abs quote" style="left:608px;top:124px"><div class="name">Tech Comp</div><div class="val">3,090.39</div><div class="dn">-8.42</div><div class="dn">-0.27%</div></div>
<div class="abs quote" style="left:665px;top:124px"><div class="name">EUR/USD</div><div class="val">1.3081</div><div class="dn">-0.00</div><div class="dn">-0.35%</div></div>
<div class="abs quote" style="left:722px;top:124px"><div class="name">10-Year Bond</div><div class="val">1.87</div><div class="dn">-0.03</div><div class="dn">-1.68%</div></div>
<div class="abs quote" style="left:779px;top:124px"><div class="name">Gold</div><div class="val">1,658.30</div><div class="up">12.00</div><div class="up">+0.73%</div></div>
<div class="abs quote" style="left:836px;top:124px"><div class="name">Oil</div><div class="val">93.22</div><div class="up">0.03</div><div class="up">+0.03%</div></div>
<svg class="abs" style="left:551px;top:160px" width="285" height="8" viewBox="0 0 285 8" fill="none" stroke="#3a6fb0" stroke-width=".8">
  <path d="M0 4 L8 3 L14 5 L22 4 L30 6 L36 4"/>
  <path d="M57 4 L65 3 L71 5 L79 4 L87 6 L93 4"/>
  <path d="M114 3 L122 5 L128 4 L136 6 L142 7 L148 5"/>
  <path d="M171 4 L179 5 L185 3 L193 4 L201 6 L207 5"/>
</svg>
<div class="abs qline" style="left:551px;top:171px;width:52px"></div>
<div class="abs qline" style="left:608px;top:171px;width:52px"></div>
<div class="abs qline" style="left:665px;top:171px;width:52px"></div>
<div class="abs qline" style="left:722px;top:171px;width:52px"></div>
<div class="abs qline up" style="left:776px;top:171px;width:54px"></div>
<div class="abs qline up" style="left:833px;top:171px;width:50px"></div>
<div class="abs more">More »</div>

<section class="abs panel" style="left:317px;top:190px;width:279px;height:256px">
  <h2 style="left:22px;top:17px">News Feed</h2>
  <div class="dots" style="left:220px;top:19px"><i class="on"></i><i></i><i></i></div>
  <div class="abs small" style="left:23px;top:46px;width:234px">
    <div class="news-item"><b>Jan 6, 2013</b><br><span class="lk">Brightkeel Labs</span> received $1,200,000 from an undisclosed investor Growth Equity</div>
    <div class="news-item"><b>Jan 5, 2013</b><br><span class="lk">Halden Works</span> merged with <span class="lk">Morrow Assurance (MRA)</span> for an Undisclosed Amount<br>Morrow Testing's parent firm and Halden Works plan to join as one grid services group, Halden Morrow, aiming to lead in storage, solar and wind project testing across markets.</div>
    <div class="news-item"><b>Jan 4, 2013</b><br><span class="lk">Tessaly Mesh</span> received an Undisclosed Amount from Quarrow Networks and Vantel Chips</div>
  </div>
  <span class="view" style="left:203px;top:232px">View All News</span>
</section>

<section class="abs panel" style="left:605px;top:190px;width:279px;height:256px">
  <h2 style="left:22px;top:17px">Company of the Month</h2>
  <div class="abs photo" role="img" aria-label="Featured company building facade" style="left:23px;top:49px;width:230px;height:97px;background:linear-gradient(90deg,#2f5f8f 0%,#4a7aa6 35%,#b9c2cc 60%,#e6e8ea 100%)"></div>
  <div class="abs small" style="left:23px;top:161px;width:234px"><span class="lk">Company Name</span> received $1,200,000 from an undisclosed investor Growth EquitySource merged with for an Undisclosed Amount<br>Morrow Testing's parent firm and Halden Works plan to join as one grid services group, Halden Morrow, aiming to lead in storage and</div>
  <span class="view" style="left:202px;top:232px">View Profile</span>
</section>

<section class="abs panel" style="left:317px;top:462px;width:279px;height:256px">
  <h2 style="left:17px;top:17px">Blog Entries</h2>
  <div class="dots" style="left:230px;top:19px"><i class="on"></i><i></i><i></i></div>

  <div class="abs post-head" style="left:20px;top:50px;width:240px"><span class="sq"></span>Company<small>Uploaded Image</small><small style="margin-left:auto">2 Minutes ago</small></div>
  <div class="abs photo" role="img" aria-label="Green seedling leaves" style="left:20px;top:78px;width:83px;height:45px;background:radial-gradient(circle at 55% 50%,#8fcf2a,#c8e87a 45%,#f4f8ec 80%)"></div>
  <div class="abs tiny" style="left:108px;top:79px;width:150px">Morrow Testing's parent firm and Halden Works plan to join as one grid services group, Halden Morrow, aiming to lead in storage and</div>
  <div class="abs tiny" style="left:108px;top:110px">Comments <span class="count">30</span></div>
  <div class="abs tiny" style="left:234px;top:112px">View All</div>

  <div class="abs post-head" style="left:20px;top:144px;width:240px"><span class="sq"></span>Company<small>Uploaded Video</small><small style="margin-left:auto">2 Minutes ago</small></div>
  <div class="abs photo" role="img" aria-label="Stack of coins video still" style="left:20px;top:171px;width:83px;height:45px;background:linear-gradient(180deg,#f5f0e8 0%,#c79a63 55%,#8a5a2e 75%,#f3efe9 100%)"></div>
  <div class="abs tiny" style="left:108px;top:171px;width:150px">Morrow Testing's parent firm and Halden Works plan to join as one grid services group, Halden Morrow, aiming to lead in storage and</div>
  <div class="abs tiny" style="left:108px;top:203px">Comments <span class="count">30</span></div>
  <div class="abs tiny" style="left:234px;top:206px">View All</div>

  <span class="view" style="left:229px;top:232px">View All</span>
</section>

<section class="abs panel" style="left:605px;top:462px;width:279px;height:256px">
  <h2 style="left:17px;top:17px">Good Reads</h2>
  <div class="dots" style="left:230px;top:19px"><i class="on"></i><i></i><i></i></div>

  <div class="abs photo" role="img" aria-label="Open book pages" style="left:18px;top:49px;width:74px;height:69px;background:linear-gradient(160deg,#fdfaf6 0%,#d9a770 40%,#7a4a22 60%,#f6efe6 100%)"></div>
  <div class="abs" style="left:100px;top:51px;font-size:7px;font-weight:700">Book</div>
  <div class="abs lorem" style="left:100px;top:65px;width:166px">Lorem ipsum dolor sit amet, consectetuer adipiscing elit, sed diam nonummy nibh euismod tincidunt ut laoreet dolore magna aliquam erat volutpat. Ut wisi enim ad minim veniam, quis nostrud exerci tation ullamcorper suscipit lobortis nisl ut aliquip ex ea commodo consequat.</div>
  <div class="abs tiny" style="left:233px;top:111px;color:var(--link)">See more</div>

  <div class="abs photo" role="img" aria-label="Seedling growing from coins in a hand" style="left:18px;top:142px;width:74px;height:69px;background:radial-gradient(circle at 50% 40%,#9fd04a 0%,#e9d3b4 45%,#f8f3ee 80%)"></div>
  <div class="abs" style="left:100px;top:144px;font-size:7px;font-weight:700">Web Site</div>
  <div class="abs lorem" style="left:100px;top:158px;width:166px">Lorem ipsum dolor sit amet, consectetuer adipiscing elit, sed diam nonummy nibh euismod tincidunt ut laoreet dolore magna aliquam erat volutpat. Ut wisi enim ad minim veniam, quis nostrud exerci tation ullamcorper suscipit lobortis nisl ut aliquip ex ea commodo consequat.</div>
  <div class="abs tiny" style="left:233px;top:205px;color:var(--link)">See more</div>

  <span class="view" style="left:231px;top:232px">View All</span>
</section>

<footer class="abs footer"></footer>
<nav class="abs foot-nav">
  <a href="#">Home</a><a href="#">K7 Profiles</a><a href="#">Forum</a><a href="#">Advisory</a><a href="#">About</a><a href="#">Contact</a><a href="#">Blog</a>
</nav>
<div class="abs follow">Follow us</div>
<div class="abs foot-social"><span></span><span></span><span></span><span></span><span></span></div>
<div class="abs brand brand-foot"><span class="mark"></span>northvale</div>

</body>
</html>
```